Chiropractic healthcare group business card

We are a Portland Oregon based chiropractic healthcare group. Looking for a new business card design. Something cutting edge, that shows off our new logo and tag line.Use either of the attached logos.Our tag line = "Where could you go without pain?"I'm open to about anything, impress me!!
Target Market(s)
Chiropractic patients - Auto injury, back pain, sports injuries, neck , shoulder, hip, knee, ankle pain.
Industry/Entity Type
Chiropractic
Contact Information for Business Card
Dr. Bram Holtvick, D.C.
Clinic name - Fernway Chiropractic
2 clinics
location #1
20418 NW Marwick Road
Suite B
North Plains, OR 97133
Location #2
13529 SE Calloway Street
Portland OR 97236
Main phone line 971.555.0143
website : www.FernwayClinics.example
Tag line "Where could you go without pain?"
Colors
Designer to choose colors to be used in the design.
Requirements
Must have
- Use the logo colors -- Want the orange color to be a TRUE orange.
- Both clinic address
- phone number
- website
- personal email - b.holtvick@ReliefBeginsHere.example
- tag line - "Where could you go without pain?"

```html
<!DOCTYPE html>
<html lang="en">
<head>
<meta charset="utf-8">
<title>Fernway Chiropractic – Business Card</title>
<link href="https://fonts.googleapis.com/css2?family=Arimo:wght@400;700&family=Crimson+Text:wght@700&family=IM+Fell+English&family=Open+Sans:wght@400&display=swap" rel="stylesheet">
<style>
  :root {
    --page: #ffffff;
    --card-front: #dcdcdc;
    --card-back: #858585;
    --orange: #f7931e;
    --ink-gray: #555555;
    --bar-gray: #666666;
    --ink-dark: #1a1a1a;
    --ink-body: #222222;
  }
  * { margin: 0; padding: 0; box-sizing: border-box; }
  html, body { width: 1000px; height: 1200px; overflow: hidden; background: var(--page); }
  body { position: relative; font-family: "Open Sans", Arial, sans-serif; }

  .card { position: absolute; left: 165px; width: 663px; height: 428px; overflow: hidden; }
  .card-front { top: 115px; background: var(--card-front); }
  .card-back { top: 655px; background: var(--card-back); }

  .wordmark { position: absolute; display: flex; align-items: center; gap: 12px; }
  .wordmark-square { width: 20px; height: 20px; background: var(--orange); flex: none; }
  .wordmark-text {
    font-family: "Arimo", Arial, sans-serif; font-weight: 700; color: var(--ink-gray);
    line-height: 1; text-transform: uppercase; white-space: nowrap;
  }
  .wordmark-text .line-main { display: block; font-size: 38px; letter-spacing: 9px; }
  .wordmark-text .line-sub { display: block; font-size: 18px; letter-spacing: 3px; margin-top: 12px; }

  .front-wordmark { left: 15px; top: 154px; }

  .doctor-name {
    position: absolute; right: 16px; top: 228px;
    font-family: "Crimson Text", Georgia, serif; font-weight: 700;
    font-size: 27px; letter-spacing: 2px; color: var(--orange); white-space: nowrap;
  }
  .clinic-line {
    position: absolute; right: 20px; top: 270px; white-space: nowrap;
    font-family: "Arimo", Arial, sans-serif; font-size: 16px; letter-spacing: 2.4px; color: var(--ink-dark);
  }
  .divider { position: absolute; left: 0; top: 302px; width: 100%; height: 7px; background: var(--bar-gray); }

  .contact-list { position: absolute; left: 20px; top: 320px; list-style: none; }
  .contact-item { display: flex; align-items: center; gap: 10px; height: 32px; font-size: 14px; color: var(--ink-body); white-space: nowrap; }
  .contact-item svg { width: 20px; height: 20px; flex: none; }

  .locations { position: absolute; right: 14px; top: 322px; text-align: right; font-size: 13.5px; line-height: 16px; color: var(--ink-body); white-space: nowrap; }
  .location-label { color: var(--orange); font-size: 14px; }
  .location + .location { margin-top: 14px; }

  .back-wordmark { left: 50%; top: 240px; transform: translateX(-50%); }
  .back-wordmark .wordmark-text { color: var(--ink-dark); }
  .tagline {
    position: absolute; left: 0; right: 0; top: 374px; text-align: center; white-space: nowrap;
    font-family: "IM Fell English", Georgia, serif; font-size: 29px; letter-spacing: 3px; color: var(--ink-dark);
  }
</style>
</head>
<body>

<section class="card card-front" aria-label="Business card front">
  <div class="wordmark front-wordmark">
    <span class="wordmark-square"></span>
    <span class="wordmark-text"><span class="line-main">Fernway</span><span class="line-sub">Chiropractic</span></span>
  </div>

  <h1 class="doctor-name">Dr. Bram Holtvick, D.C.</h1>
  <p class="clinic-line">Clinic name - Fernway Chiropractic</p>
  <div class="divider"></div>

  <ul class="contact-list">
    <li class="contact-item">
      <svg viewBox="0 0 20 20" aria-hidden="true"><path d="M5 3 L8 3 L9 7 L7 8.5 C8 11 9.5 12.5 12 13.5 L13.5 11.5 L17 12.5 L17 15.5 C17 16.5 16 17 15 17 C8.5 16.5 3.5 11.5 3 5 C3 4 4 3 5 3 Z" fill="var(--orange)"/><path d="M12 3.5 A5 5 0 0 1 16.5 8" stroke="var(--orange)" stroke-width="1.4" fill="none"/></svg>
      <span>971.555.0143</span>
    </li>
    <li class="contact-item">
      <svg viewBox="0 0 20 20" aria-hidden="true"><rect x="2.5" y="5" width="15" height="10" fill="none" stroke="var(--orange)" stroke-width="1.4"/><path d="M2.5 5 L10 11 L17.5 5" fill="none" stroke="var(--orange)" stroke-width="1.4"/></svg>
      <span>b.holtvick@ReliefBeginsHere.example</span>
    </li>
    <li class="contact-item">
      <svg viewBox="0 0 20 20" aria-hidden="true"><g fill="none" stroke="var(--orange)" stroke-width="1.3"><circle cx="10" cy="10" r="7"/><ellipse cx="10" cy="10" rx="3" ry="7"/><path d="M3 10 H17 M4.2 6.5 H15.8 M4.2 13.5 H15.8"/></g></svg>
      <span>www.FernwayClinics.example</span>
    </li>
  </ul>

  <div class="locations">
    <div class="location">
      <div class="location-label">Location #1</div>
      <div>20418 NW Marwick Road, Suite B</div>
      <div>North Plains, OR 97133</div>
    </div>
    <div class="location">
      <div class="location-label">Location #2</div>
      <div>13529 SE Calloway Street, Portland OR 97236</div>
    </div>
  </div>
</section>

<section class="card card-back" aria-label="Business card back">
  <div class="wordmark back-wordmark">
    <span class="wordmark-square"></span>
    <span class="wordmark-text"><span class="line-main">Fernway</span><span class="line-sub">Chiropractic</span></span>
  </div>
  <p class="tagline">Where could you go without pain?</p>
</section>

</body>
</html>
```